Qivora IT Company Business Card

📌 Objective:
Create a modern, fluid and stylish business card that reflects the identity of our IT company and our partnership with Veltrana.
📍 Key information:
• Company name: Qivora
• Activity: Veltrana 720 Expert
• Colors to favor: Inspired by the Qivora logo
• Style: Minimalist, modern, professional
• Front / Back:
• Items to include:
o Company logo
o Name and surname
o Post
o Email
o Phone
o Website
o QR code (optional)
🎨 Inspirations & Expectations:
• Sleek design with a high-tech touch
• Possibly subtle graphic elements linked to the Veltrana universe
• Good readability and balance between text and visuals

Lent pour commenter

Target Market(s)

Private, public

Contact Information for Business Card

Veltrana720, Formation, Gouvernance, Migration, Sécurité

Colors
6B429C
8869AF
B7A5CE
E3DAEB
F3F0F8

Requirements
Nice to have
• Have the icons of the applications I work on

```html
<!DOCTYPE html>
<html lang="en">
<head>
<meta charset="utf-8">
<title>Qivora Business Card</title>
<link rel="stylesheet" href="https://fonts.googleapis.com/css2?family=Poppins:wght@400;500;600&display=swap">
<style>
  :root {
    --page: #e6e6e8;
    --card-dark: #2b2b2d;
    --card-light: #ffffff;
    --ink: #111111;
    --emboss: #3a3a3c;
    --text-light: #ffffff;
    --accent-orange: #f15a24;
    --stripe-purple: #9b3cf0;
    --stripe-red: #ec3b5a;
    --stripe-blue: #2b9fe0;
    --shadow: rgba(0, 0, 0, 0.22);
  }
  * { box-sizing: border-box; margin: 0; padding: 0; }
  html, body {
    width: 1200px;
    height: 874px;
    overflow: hidden;
    background: var(--page);
    font-family: "Poppins", sans-serif;
  }
  .canvas {
    position: relative;
    width: 1200px;
    height: 874px;
  }
  .card {
    position: absolute;
    left: 290px;
    width: 620px;
    height: 354px;
    border-radius: 22px;
    overflow: hidden;
    box-shadow: 0 14px 30px var(--shadow);
  }

  /* Back side */
  .card-back {
    top: 53px;
    background: var(--card-dark);
    display: flex;
    align-items: center;
    justify-content: center;
  }
  .card-back .wordmark {
    font-weight: 600;
    font-size: 92px;
    letter-spacing: -2px;
    color: var(--emboss);
  }

  /* Front side */
  .card-front {
    top: 467px;
    display: flex;
    background: var(--card-dark);
  }
  .front-brand {
    width: 278px;
    background: var(--card-light);
    display: flex;
    align-items: center;
    justify-content: center;
    gap: 12px;
  }
  .brand-dot {
    width: 18px;
    height: 18px;
    border-radius: 50%;
    background: var(--stripe-red);
  }
  .front-brand .wordmark {
    font-weight: 600;
    font-size: 50px;
    letter-spacing: -1px;
    color: var(--ink);
  }
  .divider {
    width: 6px;
    display: flex;
    flex-direction: column;
  }
  .divider .seg-purple { flex: 1; background: var(--stripe-purple); }
  .divider .seg-red { flex: 1; background: var(--stripe-red); }
  .divider .seg-blue { flex: 1; background: var(--stripe-blue); }

  .front-details {
    flex: 1;
    padding: 120px 0 0 56px;
    color: var(--text-light);
  }
  .person-name {
    font-weight: 600;
    font-size: 24px;
    letter-spacing: 1px;
    line-height: 1.1;
  }
  .person-role {
    font-size: 15px;
    color: var(--accent-orange);
    margin-bottom: 26px;
  }
  .contact-list { list-style: none; }
  .contact-list li {
    display: flex;
    align-items: center;
    gap: 12px;
    font-size: 17px;
    line-height: 1.45;
  }
  .contact-list svg {
    width: 14px;
    height: 14px;
    flex: none;
    fill: var(--accent-orange);
  }
</style>
</head>
<body>
<main class="canvas">
  <section class="card card-back" aria-label="Card back">
    <span class="wordmark">Qivora</span>
  </section>

  <section class="card card-front" aria-label="Card front">
    <div class="front-brand">
      <span class="brand-dot"></span>
      <span class="wordmark">Qivora</span>
    </div>
    <div class="divider">
      <span class="seg-purple"></span>
      <span class="seg-red"></span>
      <span class="seg-blue"></span>
    </div>
    <div class="front-details">
      <p class="person-name">LENA MARLOW</p>
      <p class="person-role">President</p>
      <ul class="contact-list">
        <li>
          <svg viewBox="0 0 24 24" aria-hidden="true"><path d="M6.6 10.8a15.1 15.1 0 0 0 6.6 6.6l2.2-2.2a1 1 0 0 1 1-.25 11.4 11.4 0 0 0 3.6.57 1 1 0 0 1 1 1V20a1 1 0 0 1-1 1A17 17 0 0 1 3 4a1 1 0 0 1 1-1h3.5a1 1 0 0 1 1 1c0 1.25.2 2.45.57 3.57a1 1 0 0 1-.25 1z"/></svg>
          555-014-2290
        </li>
        <li>
          <svg viewBox="0 0 24 24" aria-hidden="true"><path d="M2 5h20v14H2z M2 5l10 8 10-8" fill="none" stroke="#f15a24" stroke-width="2.4"/><path d="M2 5h20l-10 8z"/></svg>
          info@qivora.com
        </li>
        <li>
          <svg viewBox="0 0 24 24" aria-hidden="true"><circle cx="12" cy="12" r="10" fill="none" stroke="#f15a24" stroke-width="2.4"/><path d="M2 12h20M12 2c3 3 3 17 0 20M12 2c-3 3-3 17 0 20" fill="none" stroke="#f15a24" stroke-width="2"/></svg>
          www.qivora.com
        </li>
      </ul>
    </div>
  </section>
</main>
</body>
</html>
```